Tidal Fern Business Cards

We need something new, fun and exciting for business cards. Our current ones are just plain and we need a design that pops. We want name, position held, phone, email on the front, and a 20% discount on the back. I have also uploaded our old business cards creative to see what we are not wanting, and how boring they were and we want something jazzed up from this, cool design and catches people attention.

```html
<!DOCTYPE html>
<html lang="en">
<head>
<meta charset="utf-8">
<title>Tidal Fern Business Cards</title>
<link rel="stylesheet" href="https://fonts.googleapis.com/css2?family=Montserrat:ital,wght@0,400;0,500;0,800;1,800;1,900&display=swap">
<style>
  :root {
    --navy: #1c3f6e;
    --coral: #f17270;
    --mist: #e2e2e2;
    --white: #ffffff;
  }
  * { box-sizing: border-box; margin: 0; padding: 0; }
  html, body { width: 1200px; height: 900px; overflow: hidden; background: var(--white); }
  body { position: relative; font-family: "Montserrat", sans-serif; }

  .card { position: absolute; top: 135px; width: 360px; height: 630px; overflow: hidden; background: var(--navy); }
  .card--offer { left: 199px; }
  .card--contact { left: 641px; }

  .offer-shape { position: absolute; left: 0; top: 0; width: 360px; height: 420px; }
  .offer { position: absolute; left: 108px; top: 476px; width: 145px; text-align: right; }
  .offer__value {
    display: block; font-weight: 900; font-style: italic; font-size: 62px;
    line-height: 1; color: var(--coral); letter-spacing: -2px; text-align: left;
  }
  .offer__label {
    display: block; font-weight: 800; font-style: italic; font-size: 14px;
    color: var(--white); letter-spacing: 4px; margin-top: 0;
  }

  .contact-top { position: absolute; inset: 0; width: 360px; height: 630px; }
  .brand { position: absolute; left: 0; top: 112px; width: 360px; display: flex; align-items: center; justify-content: center; gap: 12px; }
  .brand__dot { width: 22px; height: 22px; border-radius: 50%; background: var(--coral); }
  .brand__name { font-weight: 500; font-size: 40px; color: var(--navy); letter-spacing: -0.5px; line-height: 1; }

  .person { position: absolute; left: 0; top: 395px; width: 360px; text-align: center; }
  .person__name { font-weight: 800; font-size: 17px; letter-spacing: 4px; color: var(--coral); }
  .person__role { font-weight: 400; font-size: 14px; color: var(--white); margin-top: 4px; letter-spacing: 0.4px; }

  .icons { position: absolute; left: 0; top: 507px; width: 360px; display: flex; justify-content: center; gap: 3px; }
  .icons svg { width: 21px; height: 21px; }

  .details { position: absolute; left: 0; top: 537px; width: 360px; text-align: center; list-style: none; }
  .details li { font-size: 14.5px; line-height: 20px; color: var(--white); letter-spacing: 0.5px; }
  .details .accent { color: var(--coral); }
</style>
</head>
<body>

<section class="card card--offer" aria-label="Discount side">
  <svg class="offer-shape" viewBox="0 0 360 420" aria-hidden="true">
    <circle cx="250" cy="60" r="150" fill="var(--coral)"/>
  </svg>
  <p class="offer">
    <span class="offer__value">20%</span>
    <span class="offer__label">DISCOUNT</span>
  </p>
</section>

<section class="card card--contact" aria-label="Contact side">
  <svg class="contact-top" viewBox="0 0 360 630" aria-hidden="true">
    <path d="M0 0 H360 V259 C330 244 318 244 295 244 C250 244 215 270 180 306 C145 270 110 244 65 244 C42 244 25 248 0 259 Z" fill="var(--mist)"/>
    <path d="M0 259 C25 248 42 244 65 244 C110 244 145 270 180 306 C215 270 250 244 295 244 C318 244 330 244 360 259 V300 C340 278 310 262 275 262 C240 262 210 280 180 312 C150 280 120 262 85 262 C50 262 20 278 0 300 Z" fill="var(--coral)"/>
  </svg>

  <div class="brand">
    <span class="brand__dot"></span>
    <span class="brand__name">Tidal Fern</span>
  </div>

  <div class="person">
    <p class="person__name">MARA VOSS</p>
    <p class="person__role">General Manager</p>
  </div>

  <div class="icons" aria-hidden="true">
    <svg viewBox="0 0 20 20"><circle cx="10" cy="10" r="10" fill="var(--coral)"/><path d="M6.5 5.5 L8.3 5.3 L9.2 7.8 L8 8.8 C8.7 10.3 9.8 11.4 11.2 12 L12.2 10.8 L14.7 11.7 L14.5 13.5 C10 14 6 10 6.5 5.5 Z" fill="var(--white)"/></svg>
    <svg viewBox="0 0 20 20"><circle cx="10" cy="10" r="10" fill="var(--coral)"/><rect x="5" y="6.5" width="10" height="7" fill="var(--white)"/><path d="M5 6.5 L10 10.5 L15 6.5" fill="none" stroke="var(--coral)" stroke-width="0.9"/></svg>
    <svg viewBox="0 0 20 20"><circle cx="10" cy="10" r="10" fill="var(--coral)"/><g fill="none" stroke="var(--white)" stroke-width="0.9"><circle cx="10" cy="10" r="5"/><ellipse cx="10" cy="10" rx="2.2" ry="5"/><path d="M5 10 H15 M5.7 7.5 H14.3 M5.7 12.5 H14.3"/></g></svg>
  </div>

  <ul class="details">
    <li>(470) 555-0142</li>
    <li>info@tidalfern.com</li>
    <li>www.<span class="accent">tidalfern</span>.com</li>
  </ul>
</section>

</body>
</html>
```